Need to create a website for a luxury custom home builder in Phoenix USA. Looking forward for some creative designs including a full page video intro on homepage and should show up pretty luxurious.

```html
<!DOCTYPE html>
<html lang="en">
<head>
<meta charset="utf-8">
<title>Sunvale Homes – Luxury Custom Home Builder</title>
<link href="https://fonts.googleapis.com/css2?family=Poppins:wght@400;500;600;700&display=swap" rel="stylesheet">
<style>
:root{
  --teal:#17a589;
  --blue:#1e8fd6;
  --dark:#222;
  --text:#555;
  --light:#f1f3f3;
  --white:#fff;
  --cream:#ece3c8;
}
*{margin:0;padding:0;box-sizing:border-box}
html,body{width:1200px;height:4815px;overflow:hidden}
body{position:relative;font-family:'Poppins',sans-serif;color:var(--dark);background:var(--white)}
.abs{position:absolute}
.center{text-align:center}
.topbar{left:428px;top:0;width:772px;height:52px;background:var(--blue);border-bottom-left-radius:26px;color:#fff;font-size:15px}
.topbar span{position:absolute;top:15px}
.quote-top{position:absolute;left:520px;top:0;width:164px;height:52px;background:var(--teal);color:#fff;font-size:14px;line-height:52px;text-align:center}
.logo{display:flex;align-items:center;gap:10px;font-weight:700;font-size:34px;color:var(--teal);letter-spacing:1px}
.logo i{display:block;width:40px;height:40px;border-radius:50%;background:var(--blue)}
.nav a{position:absolute;top:94px;font-size:15px;color:#444;text-decoration:none}
.nav .active{color:var(--dark)}
.nav .active::after{content:"";position:absolute;left:0;right:0;bottom:-12px;height:2px;background:var(--blue)}
.hero{left:0;top:150px;width:1200px;height:661px;background:linear-gradient(180deg,#9cc7ea 0%,#dfeaf2 35%,#b6b9b3 58%,#5c9c3a 75%,#3e7f28 100%)}
.hero h1{position:absolute;left:0;right:0;top:490px;color:#fff;font-size:52px;font-weight:700;line-height:62px;text-align:center}
.play{position:absolute;left:562px;top:259px;width:76px;height:76px;border-radius:50%;border:4px solid #222;background:rgba(255,255,255,.85)}
.play::after{content:"";position:absolute;left:28px;top:18px;border-left:26px solid #222;border-top:16px solid transparent;border-bottom:16px solid transparent}
h2.title{font-size:40px;font-weight:500;line-height:48px}
.sub{font-size:14px;font-weight:600;letter-spacing:4px}
.feature{width:200px;text-align:center;font-size:15px;line-height:20px;text-transform:uppercase}
.feature .ring{width:130px;height:130px;margin:0 auto 20px;border-radius:50%;background:var(--teal);border:4px solid #fff;box-shadow:0 0 0 2px var(--teal);position:relative}
.feature .ring::after{content:"";position:absolute;inset:10px;border:2px dashed rgba(255,255,255,.8);border-radius:50%}
.feature .ring.blue{background:var(--blue);box-shadow:0 0 0 2px var(--blue)}
.para{font-size:15px;line-height:31px;color:var(--text)}
.btn{position:absolute;font-size:14px;text-align:center;text-transform:uppercase}
.photo{position:absolute}
.filters{left:350px;top:2125px;width:505px;height:43px;border-radius:22px;background:var(--teal);color:#fff;font-size:14px;font-weight:500}
.filters span{position:absolute;top:11px}
.filters .all{left:18px;top:5px;width:56px;height:33px;border-radius:17px;background:#fff;color:var(--dark);text-align:center;line-height:33px}
.card-title{font-size:16px;color:var(--teal);text-transform:uppercase}
.card-text{font-size:15px;line-height:25px;color:var(--text);text-align:justify;width:235px}
.card-link{font-size:15px;color:var(--blue)}
.arrow{position:absolute;width:40px;height:40px;border-radius:50%;border:2px solid #aaa;color:#888;font-size:22px;text-align:center;line-height:34px}
.stat{position:absolute;top:4235px;width:243px;height:190px;background:#fff;border-radius:12px;box-shadow:0 3px 14px rgba(0,0,0,.12);text-align:center}
.stat .icon{position:absolute;left:70px;top:-52px;width:104px;height:104px;border-radius:50%;background:#fff;box-shadow:0 0 0 8px #eef6fb}
.stat b{display:block;margin-top:70px;font-size:52px;font-weight:600;color:var(--teal);line-height:60px}
.stat em{font-style:normal;font-size:19px;color:var(--teal);text-transform:uppercase}
.footer{left:0;top:4335px;width:1200px;height:405px;background:var(--blue);color:#fff}
.foot-h{position:absolute;top:173px;font-size:14px;font-weight:500}
.foot-item{position:absolute;font-size:14px;line-height:18px}
.social{position:absolute;top:325px;width:34px;height:34px;border:2px solid #fff;background:rgba(255,255,255,.15)}
.copy{left:0;top:4740px;width:1200px;height:75px;background:var(--teal);color:#fff;font-size:15px;line-height:75px;text-align:center}
.cta-art{left:40px;top:3740px;width:510px;height:375px;background:linear-gradient(135deg,#c9d3dc 0%,var(--cream) 45%,#dccfa6 100%)}
</style>
</head>
<body>

<div class="abs topbar">
  <span style="left:107px">&#9742; 555-010-2040</span>
  <span style="left:272px">&#9993; hello@sunvalehomes.com</span>
  <div class="quote-top">GET FREE QUOTE</div>
</div>
<div class="abs logo" style="left:85px;top:60px"><i></i>SUNVALE HOMES</div>
<nav class="nav">
  <a class="active" style="left:625px">Home</a>
  <a style="left:708px">About</a>
  <a style="left:792px">Projects</a>
  <a style="left:888px">Service</a>
  <a style="left:982px">Blog</a>
  <a style="left:1053px">Contact</a>
</nav>

<section class="abs hero" role="img" aria-label="Video intro: modern luxury home with white and timber facade on a green lawn">
  <div class="play"></div>
  <h1>LUXURY CUSTOM HOME BUILDER<br>IN PHOENIX USA</h1>
</section>

<div class="abs" style="left:575px;top:885px;width:50px;height:50px;border-radius:50%;background:var(--blue)"></div>
<h2 class="abs title center" style="left:0;width:1200px;top:942px;font-size:34px">WHY SUNVALE HOMES IS BEST</h2>
<div class="abs feature" style="left:158px;top:1082px"><div class="ring"></div>Project<br>Management</div>
<div class="abs feature" style="left:390px;top:1082px"><div class="ring blue"></div>Building<br>Innovation</div>
<div class="abs feature" style="left:609px;top:1082px"><div class="ring"></div>Inspection &amp;<br>Testing</div>
<div class="abs feature" style="left:840px;top:1082px"><div class="ring blue"></div>New<br>Technologies</div>

<div class="abs" style="left:196px;top:1397px;width:371px;height:421px;border:2px solid var(--teal)"></div>
<div class="abs" style="left:88px;top:1423px;width:312px;height:292px;background:var(--teal)"></div>
<div class="photo" role="img" aria-label="Modern two-storey house with red timber cladding and glass balconies" style="left:100px;top:1437px;width:441px;height:358px;background:linear-gradient(135deg,#8a9aa8,#b4492b 55%,#6d7a70)"></div>
<h2 class="abs title" style="left:660px;top:1414px;color:var(--teal)">ABOUT US</h2>
<div class="abs sub" style="left:660px;top:1460px;color:var(--blue)">WHO WE WRE ——</div>
<p class="abs para" style="left:666px;top:1510px;width:456px;text-align:justify">Lorem ipsum dolor sit amet, consectetur adipiscing elit. Praesent in dictum mi. Donec gravida libero ligula, cursus suscipit ex tincidunt ac. Sed varius et erat eget vestibulum. Quisque nulla sem, feugiat nec quam et, lacinia sollici tudin tortor. Etiam malesuada fermentum mi eu vehicula. Aenean at libero tempor</p>
<div class="btn" style="left:666px;top:1732px;width:124px;height:38px;line-height:38px;background:var(--blue);color:#fff">Read More</div>
<div class="btn" style="left:805px;top:1732px;width:163px;height:38px;line-height:34px;border:2px solid var(--blue);color:var(--dark)">Get Free Quote</div>

<div class="photo" role="img" aria-label="Bright white interior room backdrop" style="left:0;top:1884px;width:1200px;height:266px;background:linear-gradient(90deg,#e4e6e6,#f7f7f7 30%,#fbfbfb 70%,#e6e8e8)"></div>
<h2 class="abs title center" style="left:0;width:1200px;top:1950px">OUR GREAT WORKS</h2>
<div class="abs sub center" style="left:0;width:1200px;top:2005px;color:var(--dark)">PROJECTS WE HAVE DONE SUCCESSFULLY</div>
<p class="abs center" style="left:200px;width:800px;top:2040px;font-size:15px;line-height:25px">Lorem ipsum dolor sit amet, consectetur adipiscing elit. Maecenas quis ultricies ligula. Aenean in lectus sed nisl vestibulum tempus.</p>
<div class="abs filters">
  <div class="all" style="position:absolute">ALL</div>
  <span style="left:97px">BUILDINGS</span>
  <span style="left:217px">CONSTRUCTION</span>
  <span style="left:366px">RENOVATION</span>
</div>

<div class="photo" role="img" aria-label="Living room with staircase and grey armchairs" style="left:85px;top:2240px;width:313px;height:300px;background:linear-gradient(160deg,#f2f2f0,#c9c6bf)"></div>
<div class="photo" role="img" aria-label="White kitchen with island" style="left:85px;top:2557px;width:313px;height:236px;background:linear-gradient(160deg,#f6f6f4,#d8d2c6)"></div>
<div class="photo" role="img" aria-label="Dark living room interior" style="left:414px;top:2240px;width:381px;height:222px;background:linear-gradient(160deg,#4c4a46,#2c2b29)">
  <div class="abs" style="left:18px;top:14px;width:345px;height:194px;border:1px solid var(--teal)"></div>
  <div class="abs center" style="left:0;width:381px;top:54px;color:#fff;font-size:24px">Ipsum dolor sit amet</div>
  <div class="abs center" style="left:118px;top:114px;width:150px;height:42px;border:1px solid #fff;color:#fff;font-size:16px;line-height:40px">View Detail</div>
</div>
<div class="photo" role="img" aria-label="Curved multi-storey building exterior" style="left:414px;top:2474px;width:381px;height:319px;background:linear-gradient(180deg,#2e3e5c,#a26a45 55%,#5c6a3c)"></div>
<div class="photo" role="img" aria-label="White kitchen with pendant lights and dark island" style="left:810px;top:2240px;width:312px;height:277px;background:linear-gradient(160deg,#f3f3f1,#8a8c8e)"></div>
<div class="photo" role="img" aria-label="Kitchen bar with gold tap and dark stools" style="left:810px;top:2531px;width:312px;height:262px;background:linear-gradient(160deg,#f4f4f2,#4a3a32)"></div>
<div class="btn" style="left:489px;top:2870px;width:222px;height:63px;line-height:63px;background:var(--teal);color:#fff;font-weight:500">View All Projects</div>

<h2 class="abs title center" style="left:0;width:1200px;top:3012px;color:var(--teal)">OUR SERVICES</h2>
<div class="abs sub center" style="left:0;width:1200px;top:3064px;color:var(--blue)">—— WHAT WE DO ——</div>
<p class="abs center" style="left:200px;width:800px;top:3098px;font-size:15px;line-height:25px">Lorem ipsum dolor sit amet, consectetur adipiscing elit. Maecenas quis ultricies ligula. Aenean in lectus sed nisl vestibulum tempus.</p>
<div class="arrow" style="left:30px;top:3370px">&lsaquo;</div>
<div class="arrow" style="left:1140px;top:3370px">&rsaquo;</div>

<div class="photo" role="img" aria-label="Construction workers in hard hats reviewing plans" style="left:85px;top:3192px;width:328px;height:342px;background:linear-gradient(160deg,#d9dde2,#b89a4a 60%,#6a5a44)"></div>
<div class="abs" style="left:85px;top:3428px;width:275px;height:200px;background:#fff"></div>
<div class="abs card-title" style="left:85px;top:3458px">Construction Service</div>
<p class="abs card-text" style="left:85px;top:3490px">Lorem ipsum dolor sit amet, consectetur adipiscing elit. Maecenas quis ultricies ligula.</p>
<div class="abs card-link" style="left:87px;top:3580px">Read More &raquo;</div>

<div class="photo" role="img" aria-label="Interior with white kitchen and window blinds" style="left:441px;top:3192px;width:327px;height:342px;background:linear-gradient(160deg,#c4b49e,#f1eee8)"></div>
<div class="abs" style="left:441px;top:3428px;width:275px;height:200px;background:#fff"></div>
<div class="abs card-title" style="left:441px;top:3458px">Interior Design</div>
<p class="abs card-text" style="left:441px;top:3490px">Lorem ipsum dolor sit amet, consectetur adipiscing elit. Maecenas quis ultricies ligula.</p>
<div class="abs card-link" style="left:443px;top:3580px">Read More &raquo;</div>

<div class="photo" role="img" aria-label="Worker renovating a house roof" style="left:796px;top:3192px;width:326px;height:342px;background:linear-gradient(160deg,#bfc9d2,#f2f2f2 50%,#8c8c8c)"></div>
<div class="abs" style="left:796px;top:3428px;width:275px;height:200px;background:#fff"></div>
<div class="abs card-title" style="left:796px;top:3458px">Home Renovations</div>
<p class="abs card-text" style="left:796px;top:3490px">Lorem ipsum dolor sit amet, consectetur adipiscing elit. Maecenas quis ultricies ligula.</p>
<div class="abs card-link" style="left:798px;top:3580px">Read More &raquo;</div>

<div class="btn" style="left:489px;top:3672px;width:222px;height:65px;line-height:65px;background:var(--blue);color:#fff;font-weight:500">View All Services</div>

<div class="abs" style="left:0;top:3848px;width:1200px;height:267px;background:var(--teal)"></div>
<div class="photo abs cta-art" role="img" aria-label="Illustration of a two-storey cream house with blue roof and red front door"></div>
<h2 class="abs center" style="left:540px;width:560px;top:3885px;color:#fff;font-size:28px;font-weight:600;line-height:36px">WE ARE READY TO SATISFY YOUR<br>PROJECT REQUIREMENTS</h2>
<p class="abs center" style="left:570px;width:500px;top:3966px;color:#fff;font-size:15px;line-height:25px">Lorem ipsum dolor sit amet, consectetur adipiscing elit. Maec enas quis ultricies ligula. Aenean in lectus</p>
<div class="btn" style="left:727px;top:4030px;width:186px;height:50px;line-height:48px;border:1px solid #fff;color:#fff">Get Your Quote</div>

<footer class="abs footer">
  <div class="abs logo" style="left:60px;top:250px;color:#fff;font-size:30px"><i style="background:#fff"></i>SUNVALE HOMES</div>
  <div class="social" style="left:93px"></div>
  <div class="social" style="left:133px"></div>
  <div class="social" style="left:173px"></div>
  <div class="social" style="left:213px"></div>

  <div class="foot-h" style="left:368px">QUICK LINKS</div>
  <div class="foot-item" style="left:368px;top:215px">&#8250; About</div>
  <div class="foot-item" style="left:368px;top:245px">&#8250; Projects</div>
  <div class="foot-item" style="left:368px;top:275px">&#8250; Services</div>
  <div class="foot-item" style="left:368px;top:305px">&#8250; Blog</div>
  <div class="foot-item" style="left:368px;top:337px">&#8250; Contact Us</div>

  <div class="foot-h" style="left:567px">CONTACT US</div>
  <svg class="abs" style="left:567px;top:218px" width="20" height="22" viewBox="0 0 20 22"><rect width="20" height="22" rx="3" fill="#fff"/><circle cx="10" cy="9" r="4" fill="#1e8fd6"/></svg>
  <div class="foot-item" style="left:600px;top:218px">Address line Dummy Here<br>Address line Here</div>
  <svg class="abs" style="left:567px;top:282px" width="20" height="20" viewBox="0 0 20 20"><rect width="20" height="20" rx="3" fill="#fff"/><path d="M6 5l3 0 1 3-2 1a7 7 0 003 3l1-2 3 1 0 3c-6 0-9-3-9-9z" fill="#1e8fd6"/></svg>
  <div class="foot-item" style="left:600px;top:283px">+555 010 2040</div>
  <svg class="abs" style="left:567px;top:332px" width="20" height="20" viewBox="0 0 20 20"><rect width="20" height="20" rx="3" fill="#fff"/><path d="M4 6h12v8H4z M4 6l6 5 6-5" fill="none" stroke="#1e8fd6" stroke-width="1.5"/></svg>
  <div class="foot-item" style="left:600px;top:333px">hello@sunvalehomes.com</div>

  <div class="foot-h" style="left:868px">OUR NEWSLETTER</div>
  <div class="foot-item" style="left:868px;top:218px;width:260px">Subscribe our newsletter to get the latest news.</div>
  <div class="abs" style="left:868px;top:273px;width:250px;height:37px;background:#fff"></div>
  <div class="abs center" style="left:868px;top:335px;width:124px;height:35px;background:var(--teal);font-size:13px;line-height:35px">SUBSCRIBE</div>
</footer>

<div class="stat" style="left:85px"><div class="icon"></div><b>453</b><em>Clients</em></div>
<div class="stat" style="left:348px"><div class="icon"></div><b>765</b><em>Recent Projects</em></div>
<div class="stat" style="left:615px"><div class="icon"></div><b>27</b><em>Awards</em></div>
<div class="stat" style="left:882px"><div class="icon"></div><b>922</b><em>Members</em></div>

<div class="abs copy">Copyright © 2023 All Rights Reserved</div>
</body>
</html>
```